Business Cards for our company

Hi there,

we have successfully designed a logo with ArtFlock and would like now to design our business cards. We would like to keep the colours and the look-and-feel of the logo. Please send in variations with two or three colours and one or two sides. I promise to respond to every single submission.

Many thanks and happy new year.

All the best,
Wilfried

Target Market(s)

B2B

Industry/Entity Type

Trade

Contact Information for Business Card

We have successfully designed a logo with ArtFlock and would like now to design our business cards. We would like to keep the colours and the look-and-feel of the logo. Please send in variations with two or three colours and one or two sides. I promise to respond to every single submission.

Font styles to use
Serif
Sans Serif
Script

Requirements
Must have
• These information should be on the business card, grouped as you suggest, and we think using small pictograms for mobile, email, etc is pretty helpful:
• Wilfried Tammler (first and second name)
• Geschäftsführer/ Managing Director (title)
• KoR Warenkontor GmbH (company name and legal form)
• Ostheimer Str. 18/3 (street and house number)
• 12345 Musterstadt (zip code and town)
• +491709384562 (mobile)
• +491239027341 (work)
• w.tammler@kor-warenkontor.example (email)
• www.kor-warenkontor.example (web)
Nice to have
• Spectacular and interesting layout and design. You look at it and think, wow, that's not the normal stuff.
• We think of ourselves as bridge-builders between businesses (international producers on the one hand, and retail chains on the other hand) and we translate, organise and manage projects where both partners are involved, but it's difficult for them to cooperate due to language barriers and different working cultures.
• This is why we have the n between the B's shaped as a bridge, and the green arc supports this idea. Maybe you could play with this idea...
Should not have
• the standard layout that everybody has

```html
<!DOCTYPE html>
<html lang="de">
<head>
<meta charset="utf-8">
<title>KoR Warenkontor – Visitenkarten</title>
<link rel="stylesheet" href="https://fonts.googleapis.com/css2?family=Open+Sans:wght@400;600;700&display=swap">
<style>
  :root {
    --backdrop: #807f80;
    --paper: #f3f3f1;
    --ink: #1a1a1a;
    --muted: #555;
    --green: #2ea84a;
    --black: #0d0d0d;
    --grey-text: #b5b5b5;
  }
  * { box-sizing: border-box; margin: 0; padding: 0; }
  html, body { width: 1200px; height: 900px; overflow: hidden; }
  body {
    background: var(--backdrop);
    font-family: "Open Sans", Arial, sans-serif;
    position: relative;
  }
  .card {
    position: absolute;
    top: 305px;
    width: 500px;
    height: 290px;
    overflow: hidden;
    box-shadow: 0 6px 18px rgba(0,0,0,.3);
  }
  .card--front { left: 70px; background: var(--paper); }
  .card--back { left: 630px; background: var(--black); }
  .card__arc { position: absolute; inset: 0; width: 100%; height: 100%; }

  .brand {
    position: absolute;
    top: 104px; left: 0; right: 0;
    text-align: center;
    color: var(--ink);
    font-weight: 700;
    line-height: 1;
  }
  .brand__name { font-size: 44px; letter-spacing: 1px; }
  .brand__sub { display: block; font-size: 15px; margin-top: 6px; letter-spacing: 1px; }

  .contact {
    position: absolute;
    left: 0; right: 0; top: 190px;
    text-align: center;
    font-size: 12px;
    color: var(--muted);
    line-height: 1.6;
  }
  .contact__address { text-transform: uppercase; letter-spacing: .3px; }
  .contact__phones {
    display: inline-block;
    border-top: 1.5px solid var(--green);
    border-bottom: 1.5px solid var(--green);
    font-weight: 600;
    color: var(--ink);
    padding: 1px 4px;
    margin: 2px 0;
  }
  .contact__tag { color: var(--green); }
  .icon {
    display: inline-block;
    width: 11px; height: 11px;
    border-radius: 50%;
    background: var(--green);
    vertical-align: -1px;
    margin: 0 3px 0 6px;
  }

  .person {
    position: absolute;
    left: 0; right: 0; top: 205px;
    text-align: center;
  }
  .person__name {
    color: var(--green);
    font-weight: 700;
    font-size: 17px;
    text-transform: uppercase;
    letter-spacing: .5px;
  }
  .person__title { color: var(--grey-text); font-size: 12px; }
</style>
</head>
<body>
  <section class="card card--front">
    <svg class="card__arc" viewBox="0 0 500 290" aria-hidden="true">
      <circle cx="250" cy="-95" r="175" fill="none" stroke="var(--green)" stroke-width="42"/>
    </svg>
    <div class="brand">
      <span class="brand__name">KoR</span>
      <span class="brand__sub">WARENKONTOR</span>
    </div>
    <div class="contact">
      <p class="contact__address">Ostheimer Str. 18/3, 12345 Musterstadt</p>
      <p class="contact__phones"><span class="icon"></span>+491709384562 <span class="contact__tag">(W)</span> <span class="icon"></span>+491239027341 <span class="contact__tag">(O)</span></p>
      <p><span class="icon"></span>w.tammler@kor-warenkontor.example <span class="icon"></span>www.kor-warenkontor.example</p>
    </div>
  </section>

  <section class="card card--back">
    <svg class="card__arc" viewBox="0 0 500 290" aria-hidden="true">
      <path d="M386 83 A150 150 0 0 1 114 83 L150 66.5 A110 110 0 0 0 350 66.5 Z" fill="var(--green)"/>
    </svg>
    <div class="person">
      <p class="person__name">Wilfried Tammler</p>
      <p class="person__title">Geschäftsführer</p>
    </div>
  </section>
</body>
</html>
```